Nature photography website

We are looking for a template for a website where we will be posting nature photography (including landscape photography, macro, and timelapse), video, and music. Website name is "BloomVistaHub".

We have a logo (attached), which should be prominently featured, and the theme should revolve around those colours/designs. Logo can be slightly modified to suit the webpage if needed. Theme colours are purple, green, blue and yellow (purple/green being most prominent), while still looking natural, to keep with a nature theme. In regards to colours, artistic discretion is fine.

We are looking for something of a high standard, so if money offered is insufficient for your best work, please submit a template and inform us of the price required to meet that standard, and we will take it into consideration. Price offered is just a rough guide. We are, however, only willing to pay extra for something that is exceptional and exactly what we're looking for.

We are looking for something that is web2.0 featuring beautiful artistic designs, not using plain colour tones. Some texture is ok, so long as it fits with the theme. We are looking for a very natural look, featuring parts of nature (ie, leaves, trees, waterfalls, flowers, stars, etc., anything that can be considered natural and looks attractive on a webpage).
Updates

Project Deadline Extended
Reason: Need more designs.

Hey guys,

I've extended the deadline to give you all more time.

Heres an example of what where after:

http://www.trelvik.example/

Heres what we like:
* The site background is nature based. its blurry as to not take away from the foreground. 
* The content box has a textured background, not a plain color.
* Beautiful illustrations around the edges of the content boxes. (WE LOVE THESE) These fit nicely over the background. We like realistic illustrations rather than cartoon art.
* A nice footer at the bottom of the page.
 
I know this is extra work guys, but we will pay more for exceptional work. Just let us know what its worth.

Ill try to post some more examples as I find them.

THANKS FOR YOUR EFFORTS SO FAR.

Mort.

Industry/Entity Type

Landscape

Requirements
Must have
• Must be attractive and eye-catching (we are not looking for anything plain).

Must prominently feature our logo (attached).

Must feature natural images and designs (not stockphoto).

CSS style sheet, etc.
Nice to have
• Multiple designs and images, not busy to the eye, but very catching and attractive.
Should not have
• Do not want plain colour tones and themes.

```html
<!DOCTYPE html>
<html lang="en">
<head>
<meta charset="utf-8">
<title>BloomVistaHub — Nature Photography</title>
<link href="https://fonts.googleapis.com/css2?family=PT+Sans:wght@400;700&display=swap" rel="stylesheet">
<style>
:root{
  --forest-dark:#24401d;
  --forest-mid:#5f8350;
  --forest-mist:#9fbd8f;
  --body-green:#4c861e;
  --body-green-light:#66a32f;
  --panel-green:#5a9a26;
  --footer-green:#24431a;
  --footer-line:#3c6a2a;
  --purple:#7b3f92;
  --purple-dark:#5e2a74;
  --orange:#f39a2c;
  --orange-light:#fbb34d;
  --orange-text:#f4a51e;
  --menu-blue:#65b2dd;
  --ink:#1f1f1f;
  --white:#ffffff;
  --photo-warm:#6a5a4c;
  --photo-dusk:#44464f;
}
*{box-sizing:border-box;margin:0;padding:0}
html,body{width:933px;height:1200px;overflow:hidden}
body{position:relative;background:#000;font-family:Arial,Helvetica,sans-serif;color:var(--white)}
.abs{position:absolute}

/* header */
.forest-backdrop{left:0;top:0;width:933px;height:411px;
  background:
    linear-gradient(90deg,rgba(20,40,15,.55) 0%,rgba(20,40,15,0) 25%,rgba(20,40,15,0) 75%,rgba(20,40,15,.45) 100%),
    linear-gradient(var(--forest-mist) 0%,var(--forest-mid) 60%,var(--forest-dark) 100%)}
.logo-box{left:145px;top:0;width:177px;height:80px;background:var(--white);border-radius:0 0 10px 10px;
  display:flex;align-items:center;justify-content:center;gap:6px;box-shadow:0 2px 6px rgba(0,0,0,.25)}
.logo-box .dot{width:10px;height:10px;border-radius:50%;background:var(--purple)}
.logo-box .name{font-family:"PT Sans",Arial,sans-serif;font-weight:700;font-size:17px;color:var(--purple)}
.search{left:672px;top:52px;width:99px;height:20px;border-radius:10px;background:#2c4a1f;border:1px solid #7aa25c;
  font-size:8px;color:#d7e6cc;padding:5px 0 0 9px}
.search svg{position:absolute;right:7px;top:5px}

.main-nav{left:145px;top:114px;width:638px;height:35px;border-radius:5px 5px 0 0;
  background:linear-gradient(var(--orange-light),var(--orange));display:flex;padding-left:14px;align-items:center}
.main-nav span{font-family:"PT Sans",Arial,sans-serif;font-size:10.5px;color:var(--ink);margin-right:10px;letter-spacing:-.1px}

.hero{left:145px;top:149px;width:638px;height:262px;
  background:linear-gradient(#474a55,var(--photo-warm) 60%,#2b2b30)}
.dropdown{left:219px;top:149px;width:128px;height:123px;background:var(--menu-blue);border-radius:0 0 5px 5px;
  border:1px solid #9fd0ee;padding-top:7px}
.dropdown li{list-style:none;font-size:8px;color:var(--ink);height:21.3px;padding-left:24px;position:relative;line-height:12px}
.dropdown li::before{content:"";position:absolute;left:12px;top:3px;width:4px;height:4px;border-right:1.5px solid var(--purple-dark);border-top:1.5px solid var(--purple-dark);transform:rotate(45deg)}
.slider-ctrl{left:159px;top:373px;width:131px;height:26px;border-radius:5px;background:linear-gradient(#fff,#ddd);
  display:flex;align-items:center;justify-content:center;gap:3px}
.slider-ctrl i{width:9px;height:9px;border-radius:50%;background:#d4d4d4;border:1px solid #aaa}
.slider-ctrl i.on{background:#555}
.slider-ctrl svg{margin:0 5px}

/* body */
.leaf-field{left:0;top:411px;width:933px;height:544px;
  background:
    radial-gradient(ellipse 40% 50% at 15% 45%,rgba(120,180,60,.35),transparent 70%),
    radial-gradient(ellipse 40% 50% at 88% 60%,rgba(120,180,60,.3),transparent 70%),
    linear-gradient(var(--body-green-light),var(--body-green))}
.panel{background:var(--panel-green);box-shadow:0 1px 4px rgba(0,0,0,.3)}
.panel-head{background:linear-gradient(#8a4aa2,var(--purple-dark));font-family:"PT Sans",Arial,sans-serif;font-size:14px;color:var(--white);height:31px;line-height:31px;border-radius:4px 4px 0 0}
.gallery{left:147px;top:438px;width:415px;height:235px}
.gallery .panel-head{padding-left:11px}
.thumb{border:2px solid #e8e8e8;background:linear-gradient(var(--photo-dusk),var(--photo-warm))}
.thumb.dim{filter:brightness(.55)}
.icon-btn{width:30px;height:30px;border-radius:5px;background:rgba(20,20,20,.7);display:flex;align-items:center;justify-content:center}

.intro-card{left:581px;top:437px;width:201px;height:236px;background:linear-gradient(#fff,#e6e6e6);border-radius:4px;color:var(--ink);padding:16px 14px 0 18px}
.intro-card h2{font-weight:400;font-size:16px;line-height:16px;margin-bottom:10px}
.intro-card p{font-size:8px;line-height:16px;color:#111}
.btn-dark{left:701px;top:644px;width:67px;height:21px;border-radius:4px;background:linear-gradient(#555,#222);font-size:8px;color:#fff;text-align:center;line-height:21px}

.lists{left:147px;top:703px;width:638px;height:229px}
.lists .panel-head{display:flex;font-family:Arial,Helvetica,sans-serif;font-size:13px}
.lists .panel-head span{width:213px;padding-left:21px}
.col-rule{top:703px;width:1px;height:229px;background:#3f7219}
.entry{width:200px;height:50px;font-weight:400}
.entry .pic{position:absolute;left:0;top:0;width:46px;height:46px;border:1px solid #3d6a1c}
.entry .t{position:absolute;left:56px;top:3px;font-size:8px;white-space:nowrap;color:#fff}
.entry .by{position:absolute;left:56px;top:19px;font-size:7.5px;color:var(--orange-text)}
.entry .by b{font-weight:400;margin-left:14px}
.entry .d{position:absolute;left:56px;top:33px;font-size:7.5px;color:#fff}

/* footer */
.footer{left:0;top:955px;width:933px;height:215px;background:linear-gradient(#27481c,var(--footer-green));border-top:1px solid var(--footer-line)}
.footer h3{font-family:"PT Sans",Arial,sans-serif;font-weight:400;font-size:12px}
.footer .q{font-size:9px;font-weight:700;color:#c5d6b8}
.footer p{font-size:8px;line-height:16px;color:#b7c9aa}
.btn-orange{width:55px;height:18px;border:1px solid #7a4a10;background:linear-gradient(var(--orange-light),#d9781a);font-size:7.5px;color:#fff;text-align:center;line-height:16px}
.mail-field{left:608px;top:1020px;width:133px;height:16px;background:#fff}
.mail-go{left:741px;top:1020px;width:18px;height:16px;background:#1e4fc8;display:flex;align-items:center;justify-content:center}
.base-band{left:0;top:1170px;width:933px;height:30px;background:#000;border-top:1px solid #2f4d25}
</style>
</head>
<body>

<header>
  <div class="abs forest-backdrop" role="img" aria-label="Blurred misty forest backdrop"></div>
  <div class="abs logo-box"><span class="dot"></span><span class="name">BloomVistaHub</span></div>
  <div class="abs search">search this site...
    <svg width="9" height="9" viewBox="0 0 10 10"><circle cx="4" cy="4" r="3" fill="none" stroke="#d7e6cc" stroke-width="1.3"/><line x1="6.2" y1="6.2" x2="9" y2="9" stroke="#d7e6cc" stroke-width="1.3"/></svg>
  </div>
  <nav class="abs main-nav">
    <span>About</span><span>Blog</span><span>Portfolio</span><span>Sitemap</span><span>Testimonials</span><span>Feedback</span><span>Contact Us</span>
  </nav>
  <div class="abs hero" role="img" aria-label="Featured landscape photograph slide"></div>
  <ul class="abs dropdown">
    <li>Wildlife Photos</li><li>Nature Photos</li><li>Cultural Photos</li><li>Adventure Photos</li><li>Portrait Photos</li>
  </ul>
  <div class="abs slider-ctrl">
    <svg width="8" height="12" viewBox="0 0 8 12"><polyline points="7,1 2,6 7,11" fill="none" stroke="#888" stroke-width="2"/></svg>
    <i></i><i></i><i class="on"></i><i></i><i></i><i></i>
    <svg width="8" height="12" viewBox="0 0 8 12"><polyline points="1,1 6,6 1,11" fill="none" stroke="#888" stroke-width="2"/></svg>
  </div>
</header>

<main>
  <div class="abs leaf-field" role="img" aria-label="Green leaf texture with swirling vine pattern"></div>

  <section class="abs panel gallery">
    <div class="panel-head">Photo Gallery</div>
  </section>
  <div class="abs thumb" style="left:157px;top:480px;width:127px;height:82px" role="img" aria-label="Gallery photo"></div>
  <div class="abs thumb dim" style="left:291px;top:480px;width:127px;height:82px" role="img" aria-label="Gallery photo"></div>
  <div class="abs icon-btn" style="left:319px;top:507px">
    <svg width="16" height="16" viewBox="0 0 16 16"><circle cx="9" cy="7" r="5" fill="none" stroke="#fff" stroke-width="2"/><line x1="5.5" y1="10.5" x2="1.5" y2="14.5" stroke="#fff" stroke-width="2.5"/></svg>
  </div>
  <div class="abs icon-btn" style="left:360px;top:507px">
    <svg width="16" height="16" viewBox="0 0 16 16"><path d="M7 3H2v11h11V9" fill="none" stroke="#fff" stroke-width="2"/><path d="M9 2h5v5M14 2L7 9" fill="none" stroke="#fff" stroke-width="2"/></svg>
  </div>
  <div class="abs thumb" style="left:426px;top:480px;width:126px;height:82px" role="img" aria-label="Gallery photo"></div>
  <div class="abs thumb" style="left:157px;top:577px;width:127px;height:83px" role="img" aria-label="Gallery photo"></div>
  <div class="abs thumb" style="left:291px;top:577px;width:127px;height:83px" role="img" aria-label="Gallery photo"></div>
  <div class="abs thumb" style="left:426px;top:577px;width:126px;height:83px" role="img" aria-label="Gallery photo"></div>

  <article class="abs intro-card">
    <h2>Lorem Ipsum is simply dummy</h2>
    <p>Lorem Ipsum is simply dummy text of the printing and typesetting industry Lorem Ipsum is simply dummy text of the printing and type-setting industry<br>Lorem Ipsum is simply dummy text of the printing and typesetting industry Lorem Ipsum is simply dummy text of the printing and type-setting industryLorem Ipsum is simply dummy text of the printing and typesetting industry</p>
  </article>
  <div class="abs btn-dark">Read More</div>

  <section class="abs panel lists">
    <div class="panel-head"><span>Popular Photos</span><span style="padding-left:16px">Random Photos</span><span style="padding-left:20px">Recent Photos</span></div>
  </section>
  <div class="abs col-rule" style="left:360px"></div>
  <div class="abs col-rule" style="left:575px"></div>

  <!-- popular -->
  <div class="abs entry" style="left:167px;top:739px"><div class="pic" style="background:#5a4e44" role="img" aria-label="Photo thumbnail"></div><div class="t">Lorem Ipsum is simply dummy</div><div class="by">Posted by <svg style="margin-left:4px" width="6" height="7" viewBox="0 0 6 7"><circle cx="3" cy="2" r="1.6" fill="#fff"/><path d="M0 7a3 3 0 0 1 6 0z" fill="#fff"/></svg> Tobias</div><div class="d">Jan 20, 2012 | 12comments</div></div>
  <div class="abs entry" style="left:167px;top:804px"><div class="pic" style="background:#3a302a" role="img" aria-label="Photo thumbnail"></div><div class="t">Lorem Ipsum is simply dummy</div><div class="by">Posted by<b>Tobias</b></div><div class="d">Jan 20, 2012 | 12comments</div></div>
  <div class="abs entry" style="left:167px;top:869px"><div class="pic" style="background:#1f1f1f" role="img" aria-label="Photo thumbnail"></div><div class="t">Lorem Ipsum is simply dummy</div><div class="by">Posted by<b>Tobias</b></div><div class="d">Jan 20, 2012 | 12comments</div></div>
  <!-- random -->
  <div class="abs entry" style="left:376px;top:739px"><div class="pic" style="background:#8a6e56" role="img" aria-label="Photo thumbnail"></div><div class="t">Lorem Ipsum is simply dummy</div><div class="by">Posted by<b>Tobias</b></div><div class="d">Jan 20, 2012 | 12comments</div></div>
  <div class="abs entry" style="left:376px;top:804px"><div class="pic" style="background:#5e4738" role="img" aria-label="Photo thumbnail"></div><div class="t">Lorem Ipsum is simply dummy</div><div class="by">Posted by<b>Tobias</b></div><div class="d">Jan 20, 2012 | 12comments</div></div>
  <div class="abs entry" style="left:376px;top:869px"><div class="pic" style="background:#352c27" role="img" aria-label="Photo thumbnail"></div><div class="t">Lorem Ipsum is simply dummy</div><div class="by">Posted by<b>Tobias</b></div><div class="d">Jan 20, 2012 | 12comments</div></div>
  <!-- recent -->
  <div class="abs entry" style="left:598px;top:739px"><div class="pic" style="background:#7a6452" role="img" aria-label="Photo thumbnail"></div><div class="t">Lorem Ipsum is simply dummy</div><div class="by">Posted by<b>Tobias</b></div><div class="d">Jan 20, 2012 | 12comments</div></div>
  <div class="abs entry" style="left:598px;top:804px"><div class="pic" style="background:#5a4234" role="img" aria-label="Photo thumbnail"></div><div class="t">Lorem Ipsum is simply dummy</div><div class="by">Posted by<b>Tobias</b></div><div class="d">Jan 20, 2012 | 12comments</div></div>
  <div class="abs entry" style="left:598px;top:869px"><div class="pic" style="background:#2e2826" role="img" aria-label="Photo thumbnail"></div><div class="t">Lorem Ipsum is simply dummy</div><div class="by">Posted by<b>Tobias</b></div><div class="d">Jan 20, 2012 | 12comments</div></div>
</main>

<footer class="abs footer">
  <h3 class="abs" style="left:152px;top:16px">FAQs</h3>
  <div class="abs q" style="left:152px;top:37px">Q: Lorem Ipsum is simply dummy</div>
  <p class="abs" style="left:151px;top:65px;width:185px">A: Lorem Ipsum is simply dummy text of the printing and typesetting industry. Lorem Ipsum has been the industry's standard dummy text ever since the 1500s, when an unknown printer</p>
  <div class="abs btn-orange" style="left:150px;top:134px">Read More...</div>

  <h3 class="abs" style="left:373px;top:16px">Blog</h3>
  <div class="abs q" style="left:376px;top:36px">Lorem Ipsum is simply dummy</div>
  <p class="abs" style="left:376px;top:49px;width:160px">Lorem Ipsum is simply dummy text of the printing and typesetting industry. Lorem Ipsum has been the industry's standard dummy text ever since the 1500s, when an unknown printer took a galley of type and</p>
  <div class="abs btn-orange" style="left:375px;top:134px">Read More...</div>

  <h3 class="abs" style="left:608px;top:15px">Newsletter</h3>
  <div class="abs" style="left:608px;top:50px;font-size:7.5px">Join our mailing list</div>
</footer>
<div class="abs mail-field">
  <svg style="position:absolute;left:5px;top:4px" width="10" height="8" viewBox="0 0 10 8"><rect x=".5" y=".5" width="9" height="7" fill="none" stroke="#bbb"/><polyline points=".5,.5 5,4.5 9.5,.5" fill="none" stroke="#bbb"/></svg>
</div>
<div class="abs mail-go"><svg width="10" height="9" viewBox="0 0 10 9"><path d="M0 4.5h8M5 1l3.5 3.5L5 8" fill="none" stroke="#fff" stroke-width="1.6"/></svg></div>
<div class="abs base-band"></div>

</body>
</html>
```